RVT studios

rvt studios is an interior design firm in omaha, NE. Offering complete residential/commercial design. Exterior, int finishes, cabinets, furniture, window covering. Have been in business for 25 yrs. Lived in and/or completed work in LA, NYC, PHX, MIami, London, Canada, Mexico. We would like to see a marketing flyer with clean, architectural design. Modern .Flyer will be on display at open houses & mailed to perspective clients. Dont want a lot of color. Prefer whites/black, greys or brown. Maybe small accent of blue like logo. Block architectural lettering. do not need to use all photos. but use at least one from each of the three projects. thanks for you time

please change/add on any and all submissions the following add: Dana Whitcombe, Principal (in info section not on logo) change: Info@rvtstudios.com, not dana @rvtstudios.com add: back design, would like to use as many photos as possible thanks you

```html
<!DOCTYPE html>
<html lang="en">
<head>
<meta charset="utf-8">
<title>RVT studios – Flyer Back</title>
<link rel="stylesheet" href="https://fonts.googleapis.com/css2?family=Caladea:wght@400;700&family=Michroma&family=Arimo:wght@700&display=swap">
<style>
  :root {
    --page-bg: #9a9a9a;
    --flyer-top: #2e2e31;
    --flyer-mid: #3a393c;
    --flyer-low: #262628;
    --footer-bg: #1c1c1d;
    --rule: #c9c9cc;
    --panel-border: #a9a9ad;
    --panel-top: #4d4b50;
    --panel-bottom: #2f2e32;
    --white: #ffffff;
    --text-light: #ececec;
    --accent-blue: #1f67b4;
    --photo-frame: #f4f4f4;
  }
  * { box-sizing: border-box; margin: 0; padding: 0; }
  html, body { width: 1200px; height: 1000px; overflow: hidden; }
  body { background: var(--page-bg); position: relative; font-family: "Caladea", Georgia, serif; }

  .flyer {
    position: absolute; left: 300px; top: 43px; width: 588px; height: 910px;
    background: linear-gradient(180deg, var(--flyer-top) 0%, var(--flyer-mid) 45%, var(--flyer-low) 100%);
    overflow: hidden;
  }

  .brand {
    position: absolute; left: 0; top: 0; width: 165px; height: 162px;
    display: flex; align-items: center; justify-content: center;
  }
  .brand-name { color: var(--white); font-size: 30px; font-weight: 400; text-align: center; line-height: 1.1; }
  .brand-divider { position: absolute; left: 162px; top: 20px; width: 4px; height: 119px; background: var(--accent-blue); }

  .headline {
    position: absolute; left: 210px; top: 30px;
    color: var(--white); font-size: 40px; font-weight: 400; line-height: 50px;
  }
  .headline strong { font-weight: 700; }

  .header-rule { position: absolute; left: 0; top: 161px; width: 100%; height: 2px; background: var(--rule); }

  .intro-panel {
    position: absolute; left: 15px; top: 191px; width: 557px; height: 222px;
    border: 2px solid var(--panel-border); border-radius: 10px;
    background: linear-gradient(180deg, var(--panel-top), var(--panel-bottom));
    padding: 22px 12px 0 15px;
  }
  .intro-text {
    font-family: "Michroma", "Arial", sans-serif; font-size: 13.5px; line-height: 29.6px;
    color: var(--text-light); text-transform: uppercase; text-align: justify; letter-spacing: 1.4px;
  }

  .gallery-rule { position: absolute; left: 0; top: 456px; width: 100%; height: 3px;
    background: linear-gradient(90deg, transparent, var(--rule) 15%, var(--rule) 85%, transparent); }
  .gallery-title {
    position: absolute; left: 128px; top: 431px; width: 326px; height: 54px;
    border: 2px solid var(--panel-border); border-radius: 4px;
    background: linear-gradient(180deg, #58565b, #3b3a3e);
    color: var(--white); font-size: 27px; font-weight: 700;
    display: flex; align-items: center; justify-content: center;
  }

  .photo { position: absolute; border: 3px solid var(--photo-frame); }
  .photo--great-room { left: 19px; top: 513px; width: 171px; height: 116px; background: linear-gradient(160deg, #4a4440, #1c1a19 70%, #6b6864); }
  .photo--bath { left: 212px; top: 513px; width: 171px; height: 116px; background: linear-gradient(180deg, #262524, #5a5856 60%, #c9c7c4); }
  .photo--wine-cellar { left: 19px; top: 645px; width: 171px; height: 115px; background: linear-gradient(120deg, #6a4a35, #2a1e17 55%, #7c7066); }
  .photo--bar { left: 212px; top: 645px; width: 171px; height: 115px; background: linear-gradient(170deg, #4c3a2c, #2a2119 55%, #8a6a45); }
  .photo--kitchen { left: 400px; top: 513px; width: 169px; height: 251px; background: linear-gradient(180deg, #b48f5e, #e3d3b1 40%, #d6c3a0 75%, #6c5842); }

  .call-line {
    position: absolute; left: 0; top: 772px; width: 100%; text-align: center;
    color: var(--accent-blue); font-size: 38px; font-weight: 700; line-height: 44px;
  }
  .call-number { font-family: "Arimo", Arial, sans-serif; color: var(--white); font-size: 29px; margin-left: 4px; }
  .call-sub {
    position: absolute; left: 0; top: 813px; width: 100%; text-align: center;
    color: var(--accent-blue); font-size: 23px; font-weight: 700;
  }

  .footer {
    position: absolute; left: 0; top: 850px; width: 100%; height: 60px; background: var(--footer-bg);
    display: flex; align-items: center; justify-content: center; gap: 6px;
    font-family: "Arimo", Arial, sans-serif; font-weight: 700; font-size: 16px; color: var(--white);
  }
  .footer-item { display: flex; align-items: center; gap: 5px; }
  .footer-item svg { width: 14px; height: 14px; fill: var(--white); }
</style>
</head>
<body>
  <main class="flyer">
    <div class="brand"><span class="brand-name">RVT studios</span></div>
    <div class="brand-divider"></div>
    <h1 class="headline"><strong>We</strong> can work<br>with your <strong>Builder</strong></h1>
    <div class="header-rule"></div>

    <section class="intro-panel">
      <p class="intro-text">We can work with your builder to coordinate the many architectural details required to create your personal space. Thus allowing your project to progress smoothly and more cost effectively.</p>
    </section>

    <div class="gallery-rule"></div>
    <h2 class="gallery-title">Our Project Gallery</h2>

    <div class="photo photo--great-room" role="img" aria-label="Photo of an open great room with dark beamed ceiling and kitchen island"></div>
    <div class="photo photo--bath" role="img" aria-label="Photo of a modern bathroom with freestanding tub and marble floor"></div>
    <div class="photo photo--wine-cellar" role="img" aria-label="Photo of a stone wine cellar with arched niche and shelving"></div>
    <div class="photo photo--bar" role="img" aria-label="Photo of a lower-level bar with curved counter and stools"></div>
    <div class="photo photo--kitchen" role="img" aria-label="Photo of a cream kitchen with carved range hood and cabinetry"></div>

    <p class="call-line">Please Call <span class="call-number">402-555-0148</span></p>
    <p class="call-sub">to Talk About Your Upcoming Project</p>

    <footer class="footer">
      <span class="footer-item">
        <svg viewBox="0 0 16 16"><path d="M1 3h14v10H1z M1 3l7 6 7-6" fill="none" stroke="#fff" stroke-width="1.6"/></svg>
        info@rvtstudios.com
      </span>
      <span class="footer-item">
        <svg viewBox="0 0 16 16"><g fill="none" stroke="#fff" stroke-width="1.3"><circle cx="8" cy="8" r="6.5"/><ellipse cx="8" cy="8" rx="2.8" ry="6.5"/><path d="M1.5 8h13M2.5 4.8h11M2.5 11.2h11"/></g></svg>
        www.rvtstudios.com
      </span>
      <span class="footer-item">
        <svg viewBox="0 0 16 16"><rect x="0.5" y="0.5" width="15" height="15" rx="3"/><path d="M5 3.5l1.6 2.4-1 1.1c.6 1.3 1.5 2.2 2.8 2.8l1.1-1 2.4 1.6-.8 1.9c-3.6-.3-6.6-3.3-6.9-6.9z" fill="#1c1c1d"/></svg>
        402-555-0148
      </span>
    </footer>
  </main>
</body>
</html>
```